Brand design for Varundel Partners

We are a new start up Fund Manager based in Singapore in need of a stylish and slick corporate identity starting with letterhead and business card (2 separate projects on craft hive but must be completed as one). We are aiming to be a somewhat 'budget' service provider with a target market of high net worth individuals and savvy self traders so we need to have our look convey value but with style. Our logo is attached and the use of the blue is imperative. The company name is Varundel Partners Pte Ltd and the verbiage 'Licensed by the Financial Oversight Board of Singapore - RFMC licence no. QRT804217-3' should be incorporated in small print.

Business card should also include address, office, direct and mobile numbers as well as email address. Follow me on twitter/fb/linkedin/Google+ should also be incrorporated. We are also looking to have a QR code on the business card that people can read with a smartphone which will auto populate our contact details in to their address book.

Many thanks and happy designing!

Reason: Extending so we can have further internal discussions. Thanks for input so far, some great designs coming through! Cheers

```html
<!DOCTYPE html>
<html lang="en">
<head>
<meta charset="utf-8">
<title>Varundel Partners – Letterhead</title>
<link rel="stylesheet" href="https://fonts.googleapis.com/css2?family=Cormorant+Garamond:wght@500&family=Crimson+Text&display=swap">
<style>
  :root {
    --paper: #ffffff;
    --skyline-light: #f5f9fc;
    --skyline-mid: #e3edf6;
    --skyline-deep: #d3e2f1;
    --water: #eef3f8;
    --ink: #111111;
  }
  * { margin: 0; padding: 0; box-sizing: border-box; }
  html, body {
    width: 840px;
    height: 1200px;
    overflow: hidden;
    background: var(--paper);
  }
  .letterhead {
    position: relative;
    width: 840px;
    height: 1200px;
    background: var(--paper);
  }
  .brand-name {
    position: absolute;
    top: 64px;
    left: 0;
    width: 840px;
    text-align: center;
    font-family: "Cormorant Garamond", serif;
    font-weight: 500;
    font-size: 40px;
    line-height: 48px;
    letter-spacing: 2px;
    color: var(--ink);
  }
  .skyline {
    position: absolute;
    top: 430px;
    left: 0;
    width: 840px;
    height: 650px;
    background:
      linear-gradient(180deg,
        var(--paper) 0%,
        var(--skyline-light) 18%,
        var(--skyline-mid) 55%,
        var(--skyline-deep) 82%,
        var(--water) 90%,
        var(--paper) 100%);
  }
  .company-footer {
    position: absolute;
    top: 1104px;
    left: 0;
    width: 840px;
    text-align: center;
    color: var(--ink);
  }
  .company-name {
    font-family: "Cormorant Garamond", serif;
    font-weight: 500;
    font-size: 29px;
    letter-spacing: 1.5px;
    line-height: 38px;
  }
  .licence-note {
    font-family: "Crimson Text", serif;
    font-size: 17px;
    line-height: 22px;
  }
</style>
</head>
<body>
  <main class="letterhead">
    <p class="brand-name">VARUNDEL PARTNERS</p>
    <div class="skyline" role="img" aria-label="Pale blue photograph of the Singapore city skyline across the river"></div>
    <footer class="company-footer">
      <p class="company-name">VARUNDEL PARTNERS Pte Ltd</p>
      <p class="licence-note">Licensed by the Financial Oversight Board of Singapore - RFMC licence no. QRT804217-3</p>
    </footer>
  </main>
</body>
</html>
```